Corvan Metalworks
Business card and stationary
Corvan Metalworks - Construction
Creative Brief
Modern
Paul Henley
Owner
4726 Birchwood Lane Washington, UT 62915
tgr.corvan@examplemail.net
www.corvanmetalworks.example
A TGR Company
We uploaded the .ai file but we like the finished look of the 2 jpeg files. 1 idea we really like is the black jpg with the chrome logo raised up on the front and on the back of the card all the information....maybe a little color....blue, red, or florescent yellow.

```html
<!DOCTYPE html>
<html lang="en">
<head>
<meta charset="utf-8">
<title>Corvan Metalworks – Business Card</title>
<link href="https://fonts.googleapis.com/css2?family=Cinzel:wght@400;600&display=swap" rel="stylesheet">
<style>
  :root {
    --backdrop: #d9d6d2;
    --card: #3a3a3b;
    --card-edge: #2e2e2f;
    --silver: #c9ccd0;
    --silver-dark: #8e9399;
    --text: #e9eaec;
    --text-soft: #b7babe;
  }
  * { margin: 0; padding: 0; box-sizing: border-box; }
  html, body {
    width: 1200px; height: 901px; overflow: hidden;
    background: var(--backdrop);
    font-family: "Cinzel", serif;
  }
  .sheet {
    width: 1200px; height: 901px;
    display: flex; align-items: center; justify-content: center; gap: 50px;
  }
  .card {
    position: relative;
    width: 525px; height: 300px;
    background: var(--card);
    border-radius: 22px;
    overflow: hidden;
    box-shadow: 0 6px 18px rgba(0,0,0,.25);
    color: var(--text);
  }
  .wordmark {
    position: absolute; left: 0; right: 0;
    display: flex; align-items: center; justify-content: center; gap: 10px;
    font-weight: 600; letter-spacing: .12em; color: var(--silver);
  }
  .wordmark-mark {
    width: 12px; height: 12px; background: var(--silver);
  }
  .card-front .wordmark { top: 132px; font-size: 26px; }
  .card-front .wordmark-mark { width: 18px; height: 18px; }
  .card-back .wordmark { top: 40px; font-size: 17px; }

  .swoosh { position: absolute; left: 0; bottom: 0; width: 525px; height: 300px; }

  .identity {
    position: absolute; right: 300px; top: 118px;
    text-align: right; width: 220px;
  }
  .identity-name { font-size: 17px; letter-spacing: .08em; }
  .identity-role { font-size: 10px; letter-spacing: .12em; color: var(--text-soft); margin-top: 3px; }
  .identity-address {
    font-size: 9px; letter-spacing: .08em; color: var(--text-soft);
    margin-top: 14px; line-height: 1.6;
  }
  .divider {
    position: absolute; left: 240px; top: 116px;
    width: 1px; height: 92px; background: var(--silver-dark);
  }
  .contacts {
    position: absolute; left: 254px; top: 116px;
    list-style: none; font-size: 9.5px; letter-spacing: .06em;
  }
  .contacts li { display: flex; align-items: center; gap: 7px; height: 18px; }
  .contact-icon { width: 11px; height: 11px; flex: none; }
</style>
</head>
<body>
<main class="sheet">
  <section class="card card-front" aria-label="Card front">
    <div class="wordmark"><span class="wordmark-mark"></span>Corvan Metalworks</div>
  </section>

  <section class="card card-back" aria-label="Card back">
    <svg class="swoosh" viewBox="0 0 525 300" aria-hidden="true">
      <defs>
        <linearGradient id="chrome" x1="0" y1="0" x2="1" y2="0">
          <stop offset="0" stop-color="#eef0f2"/>
          <stop offset=".5" stop-color="#b9bdc2"/>
          <stop offset="1" stop-color="#7d8288"/>
        </linearGradient>
      </defs>
      <path d="M0 232 C120 206 210 238 300 262 C360 278 420 286 525 282 L525 300 L0 300 Z" fill="#575a5e"/>
      <path d="M0 238 C110 214 200 246 290 270 C350 286 410 294 525 292 L525 300 L0 300 Z" fill="url(#chrome)"/>
      <path d="M0 256 C120 240 200 270 280 290 L280 300 L0 300 Z" fill="#6b6f74"/>
    </svg>

    <div class="wordmark"><span class="wordmark-mark"></span>Corvan Metalworks</div>

    <div class="identity">
      <p class="identity-name">Paul Henley</p>
      <p class="identity-role">Owner</p>
      <p class="identity-address">4726 Birchwood Lane<br>Washington, UT 62915</p>
    </div>

    <div class="divider"></div>

    <ul class="contacts">
      <li><svg class="contact-icon" viewBox="0 0 12 12"><circle cx="6" cy="6" r="6" fill="#e9eaec"/><path d="M4 3.2l1 1.4-.6.7c.4.9 1 1.5 1.9 1.9l.7-.6 1.4 1-.5 1.2C5.6 8.7 3.3 6.4 3 4.1z" fill="#3a3a3b"/></svg>435-555-0142</li>
      <li><svg class="contact-icon" viewBox="0 0 12 12"><circle cx="6" cy="6" r="6" fill="#e9eaec"/><rect x="4" y="2.5" width="4" height="7" rx=".8" fill="#3a3a3b"/></svg>435-555-0187</li>
      <li><svg class="contact-icon" viewBox="0 0 12 12"><circle cx="6" cy="6" r="6" fill="#e9eaec"/><rect x="3" y="4" width="6" height="4.5" fill="#3a3a3b"/><rect x="4" y="2.5" width="4" height="1.5" fill="#3a3a3b"/></svg>435-555-0163</li>
      <li><svg class="contact-icon" viewBox="0 0 12 12"><circle cx="6" cy="6" r="6" fill="#e9eaec"/><rect x="3" y="4" width="6" height="4" fill="#3a3a3b"/><path d="M3 4l3 2.2L9 4" stroke="#e9eaec" stroke-width=".6" fill="none"/></svg>tgr.corvan@examplemail.net</li>
      <li><svg class="contact-icon" viewBox="0 0 12 12"><circle cx="6" cy="6" r="6" fill="#e9eaec"/><circle cx="6" cy="6" r="3" fill="none" stroke="#3a3a3b" stroke-width=".8"/><path d="M3 6h6M6 3v6" stroke="#3a3a3b" stroke-width=".6"/></svg>www.corvanmetalworks.example</li>
    </ul>
  </section>
</main>
</body>
</html>
```